Horse related business entrepreneur needs a business card

I need a business card design for my horse related business. The enterprise is Copper Vale LLC and I have 3 businesses (headquartered at 2 locations): 1. property management where we rent horse stalls and apartments at a thoroughbred training center outside Ocala; 2. a medium sized transportation service in central Florida that sells horse bedding and removes used horse bedding from horse farms; and horse racing

```html
<!DOCTYPE html>
<html lang="en">
<head>
<meta charset="utf-8">
<title>Copper Vale LLC — Business Card</title>
<link rel="stylesheet" href="https://fonts.googleapis.com/css2?family=Libre+Baskerville:wght@400;700&family=Montserrat:wght@500;600;700&display=swap">
<style>
  :root {
    --backdrop: #4b4b4b;
    --ink-dark: #231f20;
    --paper: #ffffff;
    --brand-red: #c1272d;
    --rule-red: #e08a8d;
    --text-dark: #231f20;
  }
  * { margin: 0; padding: 0; box-sizing: border-box; }
  html, body {
    width: 1040px; height: 1200px; overflow: hidden;
    background: var(--backdrop);
  }
  .canvas { position: relative; width: 1040px; height: 1200px; }

  .card {
    position: absolute; left: 32px; width: 976px;
    background: var(--ink-dark); overflow: hidden;
  }
  .card--front { top: 27px; height: 560px; }
  .card--back  { top: 613px; height: 552px; }

  .wordmark {
    font-family: "Libre Baskerville", serif;
    font-weight: 700; color: var(--paper);
    text-align: center; line-height: 1;
    letter-spacing: 0.04em; text-transform: uppercase;
  }
  .wordmark__suffix {
    display: flex; align-items: center; justify-content: center;
    letter-spacing: 0.12em;
  }
  .wordmark__suffix::before,
  .wordmark__suffix::after {
    content: ""; height: 3px; background: var(--paper);
  }
  .card--front .wordmark {
    position: absolute; top: 52px; left: 0; right: 0; font-size: 58px;
  }
  .card--front .wordmark__suffix { font-size: 26px; margin-top: 8px; }
  .card--front .wordmark__suffix::before { width: 150px; margin-right: 18px; }
  .card--front .wordmark__suffix::after  { width: 40px; margin-left: 14px; }

  .front__panel {
    position: absolute; top: 213px; left: 0; right: 0; height: 334px;
    background: var(--paper);
  }
  .holder { position: absolute; left: 53px; top: 42px; font-family: "Montserrat", sans-serif; color: var(--text-dark); }
  .holder__name { font-size: 38px; font-weight: 500; letter-spacing: 0.03em; }
  .holder__rule { width: 135px; height: 3px; background: var(--rule-red); margin: 10px 0 14px; }
  .holder__title { font-size: 30px; font-weight: 600; }

  .contacts { position: absolute; right: 21px; top: 32px; list-style: none; font-family: "Montserrat", sans-serif; }
  .contacts__item {
    display: flex; align-items: center; justify-content: flex-end;
    height: 48px; margin-bottom: 38px;
    font-size: 25px; font-weight: 700; color: var(--text-dark);
  }
  .contacts__icon {
    width: 48px; height: 48px; margin-left: 26px;
    background: var(--brand-red); color: var(--paper);
    display: flex; align-items: center; justify-content: center;
    font-size: 28px; font-weight: 700;
  }

  .tagline-band { position: absolute; left: 0; bottom: 0; width: 976px; height: 50px; }
  .tagline {
    position: absolute; left: 0; right: 0; bottom: 8px; text-align: center;
    font-family: "Libre Baskerville", serif; font-size: 23px; color: var(--paper);
  }

  .card--back .wordmark { position: absolute; top: 112px; left: 0; right: 0; font-size: 92px; }
  .card--back .wordmark__suffix { font-size: 44px; margin-top: 18px; }
  .card--back .wordmark__suffix::before { width: 280px; margin-right: 28px; }
  .card--back .wordmark__suffix::after  { width: 60px; margin-left: 22px; }

  .addresses {
    position: absolute; left: 0; right: 0; top: 402px; text-align: center;
    font-family: "Montserrat", sans-serif; font-weight: 700; font-size: 25px;
    color: var(--brand-red); font-style: normal; line-height: 52px;
  }
  .addresses sup { font-size: 15px; }
</style>
</head>
<body>
<main class="canvas">
  <section class="card card--front" aria-label="Business card front">
    <div class="wordmark">Copper Vale<span class="wordmark__suffix">LLC</span></div>

    <div class="front__panel">
      <div class="holder">
        <h1 class="holder__name">MARCUS HALE</h1>
        <div class="holder__rule"></div>
        <p class="holder__title">Owner</p>
      </div>

      <ul class="contacts">
        <li class="contacts__item">marcus@coppervale.com
          <span class="contacts__icon" aria-label="Email">
            <svg width="28" height="22" viewBox="0 0 28 22" aria-hidden="true">
              <rect x="1" y="1" width="26" height="20" fill="none" stroke="#fff" stroke-width="2.5"/>
              <path d="M1 2 L14 12 L27 2" fill="none" stroke="#fff" stroke-width="2.5"/>
            </svg>
          </span>
        </li>
        <li class="contacts__item">(352) 618 2047<span class="contacts__icon" aria-label="Phone">P</span></li>
        <li class="contacts__item">(352) 618 2093<span class="contacts__icon" aria-label="Fax">F</span></li>
      </ul>
    </div>

    <svg class="tagline-band" viewBox="0 0 976 50" aria-hidden="true">
      <rect x="0" y="0" width="976" height="50" fill="#231f20"/>
      <polygon points="232,0 744,0 720,50 256,50" fill="#ffffff"/>
      <polygon points="252,0 724,0 702,50 274,50" fill="#c1272d"/>
    </svg>
    <p class="tagline">Horse Country Holdings</p>
  </section>

  <section class="card card--back" aria-label="Business card back">
    <div class="wordmark">Copper Vale<span class="wordmark__suffix">LLC</span></div>
    <address class="addresses">
      <p>1720 NW 92<sup>nd</sup> Terrace, Fairhaven, FL 32671</p>
      <p>5815 Willow Ridge Lane, Ashford, VA 22903</p>
    </address>
  </section>
</main>
</body>
</html>
```